Design an App Mockup for Restaurant

Design:

I have built a mobile app for my client. I require 5 mobile screens to be designed.

Please see the attached files for description and guidelines.

I have attached a picture of my clients logo to provide ideas for the colour scheme.

Please let me know if you have any questions.

```html
<!DOCTYPE html>
<html lang="en">
<head>
<meta charset="utf-8">
<title>Saffron Table – Home Screen</title>
<link rel="stylesheet" href="https://fonts.googleapis.com/css2?family=Roboto:wght@300;400;700&display=swap">
<style>
  :root {
    --page-bg: #e9eaec;
    --status-bg: #1f2a33;
    --title-bg-top: #b9bdc1;
    --title-bg-bottom: #a4a9ae;
    --screen-top: #27394a;
    --screen-mid: #2c5566;
    --screen-bottom: #3f7d76;
    --text-light: #f2f5f6;
    --divider: rgba(255,255,255,0.28);
    --accent-green: #8cc63f;
    --icon-dark: #1d2a30;
    --banner-a: #f3c23a;
    --banner-b: #e59a1c;
    --banner-c: #a8324a;
  }
  * { margin: 0; padding: 0; box-sizing: border-box; }
  html, body { width: 1200px; height: 939px; overflow: hidden; }
  body {
    background: var(--page-bg);
    font-family: "Roboto", Arial, sans-serif;
    position: relative;
  }
  .app-screen {
    position: absolute;
    left: 353px; top: 30px;
    width: 494px; height: 878px;
    background: linear-gradient(180deg, var(--screen-top) 0%, var(--screen-mid) 55%, var(--screen-bottom) 100%);
    overflow: hidden;
    box-shadow: 0 10px 30px rgba(0,0,0,0.18);
  }
  .status-bar {
    height: 30px;
    background: var(--status-bg);
    color: var(--text-light);
    font-size: 15px;
    display: flex; align-items: center; justify-content: space-between;
    padding: 0 14px;
  }
  .status-bar .time { font-weight: 700; }
  .status-bar .carrier, .status-bar .battery { display: flex; align-items: center; gap: 6px; }
  .title-bar {
    height: 57px;
    background: linear-gradient(180deg, var(--title-bg-top), var(--title-bg-bottom));
    color: #fff;
    font-size: 27px; font-weight: 300;
    display: flex; align-items: center; justify-content: center;
  }
  .promo-banner {
    position: absolute;
    left: 31px; top: 134px;
    width: 434px; height: 202px;
    background: radial-gradient(circle at 28% 55%, #fbf3e4 0 16%, transparent 17%),
                radial-gradient(circle at 68% 38%, var(--banner-c) 0 9%, transparent 10%),
                linear-gradient(120deg, var(--banner-a), var(--banner-b));
  }
  .promo-banner .promo-text {
    position: absolute; right: 10px; top: 118px;
    font-size: 26px; color: #111; letter-spacing: 0.5px;
  }
  .promo-banner .promo-text b { font-weight: 700; }
  .brand-name {
    position: absolute; left: 0; right: 0; top: 398px;
    text-align: center;
    font-size: 34px; font-weight: 300; color: var(--accent-green);
  }
  .main-menu {
    position: absolute; left: 40px; top: 458px; width: 416px;
    list-style: none;
    border-top: 1px solid var(--divider);
  }
  .main-menu li {
    height: 67px;
    border-bottom: 1px solid var(--divider);
    display: flex; align-items: center; justify-content: center;
    color: var(--text-light);
    font-size: 32px; font-weight: 300; letter-spacing: 0.5px;
  }
  .tab-bar {
    position: absolute; left: 0; right: 0; bottom: 0; height: 96px;
    display: flex; justify-content: space-around; align-items: center;
    padding: 0 10px;
  }
  .tab-bar svg { width: 62px; height: 62px; }
  .tab-indicator {
    position: absolute; left: 60px; bottom: 0;
    width: 0; height: 0;
    border-left: 7px solid transparent; border-right: 7px solid transparent;
    border-bottom: 7px solid var(--accent-green);
  }
</style>
</head>
<body>
  <main class="app-screen">
    <div class="status-bar">
      <span class="carrier">
        <svg width="46" height="10" viewBox="0 0 46 10"><g fill="#fff"><circle cx="5" cy="5" r="4"/><circle cx="14" cy="5" r="4"/><circle cx="23" cy="5" r="4"/></g><g fill="none" stroke="#fff"><circle cx="32" cy="5" r="3.5"/><circle cx="41" cy="5" r="3.5"/></g></svg>
        NOVA
      </span>
      <span class="time">4:21 PM</span>
      <span class="battery">22%
        <svg width="34" height="14" viewBox="0 0 34 14"><rect x="1" y="1" width="28" height="12" rx="2" fill="none" stroke="#fff"/><rect x="3" y="3" width="6" height="8" fill="#fff"/><rect x="30" y="4.5" width="3" height="5" fill="#fff"/></svg>
      </span>
    </div>
    <header class="title-bar">Saffron Table</header>

    <div class="promo-banner" role="img" aria-label="Lunch dish photograph with cream and berries on a golden sauce">
      <span class="promo-text"><b>LUNCH</b> IS SERVED!</span>
    </div>

    <div class="brand-name">Saffron</div>

    <ul class="main-menu">
      <li>PICK UP</li>
      <li>DELIVERY</li>
      <li>DINE IN</li>
      <li>VIEW MENU</li>
    </ul>

    <nav class="tab-bar">
      <svg viewBox="0 0 62 62" aria-label="Home"><g fill="none" stroke="var(--icon-dark)" stroke-width="2.5"><path d="M10 30 L31 10 L52 30"/><path d="M17 24 V52 H45 V24"/><path d="M27 52 V38 H35 V52"/></g></svg>
      <svg viewBox="0 0 62 62" aria-label="Help"><circle cx="31" cy="31" r="24" fill="none" stroke="var(--icon-dark)" stroke-width="2.5"/><text x="31" y="41" text-anchor="middle" font-family="Roboto, sans-serif" font-size="28" fill="var(--icon-dark)">?</text></svg>
      <svg viewBox="0 0 62 62" aria-label="Support"><g fill="none" stroke="var(--icon-dark)" stroke-width="2.5"><path d="M15 34 V28 a16 16 0 0 1 32 0 V34"/><rect x="12" y="30" width="7" height="12" rx="3"/><rect x="43" y="30" width="7" height="12" rx="3"/><path d="M46 42 q0 8 -12 8"/><circle cx="31" cy="50" r="3"/></g></svg>
      <svg viewBox="0 0 62 62" aria-label="Account"><g fill="none" stroke="var(--icon-dark)" stroke-width="2.5"><circle cx="31" cy="31" r="24"/><circle cx="31" cy="25" r="8"/><path d="M16 48 q15 -18 30 0"/></g></svg>
    </nav>
    <span class="tab-indicator"></span>
  </main>
</body>
</html>
```